Awesome Web Design Project

must have a link to mingleton of the homepage preferably a scrolling view of our mingleton page!

We are an exciting new electrical company with a strong focus on energy efficiency and offering the latest technologies.

The design should allow easy navigation, there shouldn't be too many menus, It should look clean and sleek, Colours to consider could be green, silver/chrome, black,

The site should convey technology, efficiency and simplicity

Must be viewable on all devices, pc's, tablets, phones ie Responsive
Updates

Logo and some pics uploaded!

Industry/Entity Type

Electrical

Requirements
Must have
• must include the following pages,
about us
our services
gallery
contact us
Connect with us
Nice to have
• Would be great if the website design used a user friendly cms,
Should not have
• too many links, menus, clutter it should be clean and easy to navigate

```html
<!DOCTYPE html>
<html lang="en">
<head>
<meta charset="utf-8">
<title>Kestrel Electrical</title>
<link href="https://fonts.googleapis.com/css2?family=Arimo:wght@400;700&family=Roboto+Condensed:wght@300&display=swap" rel="stylesheet">
<style>
:root{
  --lime:#d6de23;
  --teal-dark:#073a3f;
  --teal-mid:#2f6168;
  --teal-light:#5e8289;
  --ink:#222;
  --nav-top:#5a5a5a;
  --nav-bottom:#353535;
  --footer:#333;
  --white:#fff;
}
*{box-sizing:border-box;margin:0;padding:0}
html,body{width:1200px;height:868px;overflow:hidden}
body{font-family:"Arimo",Arial,sans-serif;color:var(--ink);background:linear-gradient(#fff 0,#fff 540px,#dcdcdc 817px)}
.wrap{width:900px;margin:0 auto;position:relative}

.site-header{height:87px;background:linear-gradient(#fff,#d8d8d8)}
.site-header .wrap{height:87px}
.brand{position:absolute;left:0;top:27px;display:flex;align-items:center;gap:8px;font-weight:700;font-size:22px;color:var(--teal-dark);letter-spacing:1px}
.brand .mark{width:31px;height:31px;background:var(--lime)}
.contact-bar{position:absolute;right:0;top:14px;display:flex;align-items:center;gap:6px;font-size:13px}
.contact-bar .social{display:flex;gap:4px;margin-left:12px}
.social a{width:18px;height:18px;display:block;border-radius:2px}
.social .mingleton{background:#3b5998}
.social .chirpline{background:#5bc4e6}
.main-nav{position:absolute;right:0;top:41px;display:flex;height:32px;border-radius:4px;overflow:hidden;background:linear-gradient(var(--nav-top),var(--nav-bottom))}
.main-nav a{display:flex;align-items:center;justify-content:center;color:var(--white);text-decoration:none;font-weight:700;font-size:12px;border-left:1px solid #1c1c1c}
.main-nav a:first-child{border-left:0}

.hero{height:400px;background:linear-gradient(var(--teal-dark),var(--teal-mid) 45%,var(--teal-light))}
.hero .wrap{height:400px}
.hero h1{position:absolute;left:0;top:68px;font-family:"Roboto Condensed",sans-serif;font-weight:300;font-size:28px;line-height:36px;color:var(--lime);white-space:nowrap}
.hero p{position:absolute;left:0;top:160px;width:420px;font-size:15px;line-height:23.5px;color:var(--white)}
.cta{position:absolute;left:0;top:274px;width:180px;height:32px;display:flex;align-items:center;padding-left:18px;font-weight:700;font-size:13px;color:var(--teal-dark);text-decoration:none;background:var(--lime);clip-path:polygon(0 0,160px 0,180px 32px,0 32px);border-radius:3px 0 0 3px;white-space:nowrap}
.hero-photo{position:absolute;left:427px;top:58px;width:473px;height:283px;border:3px solid #333;box-shadow:0 2px 8px rgba(0,0,0,.6);background:linear-gradient(#f2f2f2,#b9bcbe 55%,#5a5550)}

.recent{height:330px}
.recent .wrap{height:330px}
.recent h2{text-align:center;padding-top:48px;font-size:30px;color:var(--teal-dark);font-weight:700}
.works{position:absolute;left:0;top:106px;display:flex;gap:19px}
.work{width:211px;height:141px;border:1px solid #bbb;border-radius:3px;background:#fff;padding:4px;position:relative}
.work.active{border-color:var(--teal-dark)}
.work .pic{width:100%;height:100%}
.pic.hall{background:linear-gradient(#e8eced,#c2c7c8)}
.pic.beams{background:linear-gradient(135deg,#c9c6b5,#8d8066 50%,#d9d7c4)}
.pic.lounge{background:linear-gradient(#b97a60,#c8b6a3 60%,#7a6b5a)}
.pic.glow{background:linear-gradient(#1b2a6d,#2137c8 55%,#7a4c2c)}
.tip{position:absolute;left:91px;top:123px;width:145px;height:22px;border:1px solid #777;border-radius:2px;background:linear-gradient(#f4f4f4,#c9c9c9);font-size:10px;line-height:20px;padding-left:7px;color:#111;white-space:nowrap}
.view-all{position:absolute;right:0;top:258px;font-size:13px;font-style:italic;color:var(--teal-dark);border-bottom:1px solid var(--teal-dark);text-decoration:none}

.site-footer{position:absolute;left:0;top:817px;width:1200px;height:51px;background:var(--footer);display:flex;justify-content:center;align-items:center}
.site-footer nav{display:flex;font-size:12px;color:var(--white)}
.site-footer nav a,.site-footer nav span{color:var(--white);text-decoration:none;padding:0 15px;border-left:1px solid #777;line-height:16px}
.site-footer nav a:first-child{border-left:0}
</style>
</head>
<body>
<header class="site-header">
  <div class="wrap">
    <a class="brand"><span class="mark"></span>Kestrel Electrical</a>
    <div class="contact-bar">
      <svg width="11" height="17" viewBox="0 0 11 17"><path d="M3 1h3l1 4-2 1.5c.5 2 1.5 3.5 3 4.5L10 10l1 4-1 2C5 16 1 10 1 3z" fill="#2f6168"/></svg>
      <span>+61 2 5550 0147</span>
      <span class="social"><a class="mingleton" aria-label="mingleton"></a><a class="chirpline" aria-label="chirpline"></a></span>
    </div>
    <nav class="main-nav">
      <a style="width:97px">ABOUT US</a>
      <a style="width:95px">SERVICES</a>
      <a style="width:91px">GALLERY</a>
      <a style="width:110px">CONTACT US</a>
      <a style="width:94px">CONNECT</a>
    </nav>
  </div>
</header>

<section class="hero">
  <div class="wrap">
    <h1>We offer the latest technologies with<br>a strong focus on energy efficiency</h1>
    <p>Lorem ipsum dolor sit amet, consectetur adipiscing elit. Fusce felis elit, imperdiet tempus ornare aliquet, lacinia a erat. Nunc iaculis ornare vehicula. Pellentesque iaculis velit quis felis tristique sollicitudin pellentesque habitant morbi.</p>
    <a class="cta">Learn what we can do</a>
    <div class="hero-photo" role="img" aria-label="Modern interior with angular linear ceiling lights"></div>
  </div>
</section>

<section class="recent">
  <div class="wrap">
    <h2>Recent Works</h2>
    <div class="works">
      <div class="work active"><div class="pic hall" role="img" aria-label="Bright commercial fit-out with ceiling lighting"></div><div class="tip">the title of this Project/Picture</div></div>
      <div class="work"><div class="pic beams" role="img" aria-label="Timber roof beams with warm uplighting"></div></div>
      <div class="work"><div class="pic lounge" role="img" aria-label="Home entertainment setup against a brick wall"></div></div>
      <div class="work"><div class="pic glow" role="img" aria-label="Blue LED strip lighting under cabinetry"></div></div>
    </div>
    <a class="view-all">View All »</a>
  </div>
</section>

<footer class="site-footer">
  <nav>
    <a>Home</a><a>About Us</a><a>Services</a><a>Gallery</a><a>Contact Us</a><a>Connect</a><span>©2013 Kestrel Electrical.</span>
  </nav>
</footer>
</body>
</html>
```